Website needed for Entertainment Company [Wordpress & Mobile Site] (Contest)

"Tumble Scholars" does Acrobatic Educational Shows for schools.
We need a 4-Page Wordpress site, for BOTH Desktop & Mobile
THINGS WE'D LIKE ON THE HOME PAGE
- Book Now buttons
- Panel advertising "Kindness-Shield Tumbling Tour" with subheading "Educating the Victim, Empowering the Bystander, and Enlightening the Bully" with Photo & 'Read More'
- text somewhere saying "Tumble Scholars engages children in important topics, by utilising Parkour & Acrobatics to captivate and enthrall todays youngest generation."
- Panel advertising Teachers Resources: "Curriculum based resources for teachers including lesson plans, workbooks, and physical activities for before & after the show." Maybe even some boxes that say a subject that is covered (eg. Mathematics. Science. PD/H/PE.)
- Everything else that you recommend
4 PAGES:
- Home Page
- About Us
- Our Program & Shows
- Teachers Resources Portal
NOTE: Transparent & Source files for logo will be provided soon (recently finished being designed)

```html
<!DOCTYPE html>
<html lang="en">
<head>
<meta charset="utf-8">
<title>Tumble Scholars – Acrobatic Educational Shows</title>
<link href="https://fonts.googleapis.com/css2?family=Montserrat:wght@400;500;600;700&display=swap" rel="stylesheet">
<style>
:root{
  --ink:#1f1f1f;
  --muted:#8a8a8a;
  --white:#ffffff;
  --orange-a:#f4b21c;
  --orange-b:#ea5a1e;
  --teal:#2aa6d6;
  --yellow:#e9a81c;
  --yellow-soft:#f3d48c;
  --purple:#a68ee8;
  --purple-soft:#d6cbf5;
  --green:#a9c21f;
  --green-soft:#d8e48f;
  --grey:#6d6d6d;
  --grey-soft:#b9b9b9;
  --footer:#231f20;
  --footer-text:#9b9b9b;
  --accent:#2aa6d6;
}
*{box-sizing:border-box;margin:0;padding:0}
html,body{width:1200px;height:2715px;overflow:hidden}
body{font-family:"Montserrat",sans-serif;color:var(--ink);background:var(--white);position:relative}
.abs{position:absolute}

/* header */
.site-header{position:absolute;left:0;top:0;width:1200px;height:94px;z-index:3}
.brand{position:absolute;left:69px;top:28px;font-weight:700;font-size:22px;color:var(--orange-a);letter-spacing:.3px}
.main-nav{position:absolute;top:38px;left:471px;display:flex;gap:0}
.main-nav a{position:absolute;white-space:nowrap;color:var(--white);text-decoration:none;font-size:12.5px;font-weight:500}
.main-nav .current{color:var(--teal)}
.btn-book{position:absolute;left:970px;top:31px;width:159px;height:33px;border-radius:17px;background:linear-gradient(90deg,var(--orange-a),var(--orange-b));color:var(--ink);font-size:12px;font-weight:600;display:flex;align-items:center;justify-content:center;text-decoration:none}

/* hero */
.hero{position:absolute;left:0;top:0;width:1200px;height:720px;background:
  linear-gradient(180deg,#050505 0%,#0c0a08 45%,#3a2614 72%,#8a5a2e 88%,#6b4322 100%)}
.hero h1{position:absolute;left:141px;top:284px;font-weight:400;font-size:40px;line-height:46px;color:var(--white)}
.btn-hero{position:absolute;left:141px;top:501px;width:126px;height:36px;border-radius:18px;background:linear-gradient(90deg,var(--orange-a),var(--orange-b));color:var(--ink);font-size:12px;font-weight:600;display:flex;align-items:center;justify-content:center}

/* show intro */
.show-intro{position:absolute;left:0;top:720px;width:1200px;height:840px}
.show-intro .halo{position:absolute;left:436px;top:37px;width:326px;height:326px;border-radius:50%;background:#f3f3f3}
.show-intro h2{position:absolute;left:0;width:1200px;top:109px;text-align:center;font-size:24px;line-height:29px;font-weight:700}
.show-intro p{position:absolute;left:285px;width:630px;top:181px;text-align:center;font-size:12.2px;line-height:19px;color:var(--muted)}
.explore{position:absolute;left:527px;width:144px;top:289px;text-align:center;font-size:11.5px;font-weight:600;padding-bottom:14px;border-bottom:2px solid var(--accent)}

.theme-card{position:absolute;top:400px;width:281px;height:361px;overflow:hidden}
.theme-card h3{position:absolute;left:0;width:100%;text-align:center;color:var(--white);font-size:24px;line-height:29px;font-weight:700}
.theme-card .rule{position:absolute;left:50%;width:50px;margin-left:-25px;height:2px;background:var(--white)}
.card-victim{left:139px;background:linear-gradient(160deg,#1b6e78 0%,#0f4e58 55%,#2b2f4a 100%)}
.card-victim h3{top:258px}
.card-bystander{left:460px;background:linear-gradient(180deg,#bfd3e2 0%,#8b8f98 40%,#4b4a55 100%);box-shadow:0 22px 40px rgba(0,0,0,.25)}
.card-bystander h3{top:92px}
.card-bystander .rule{top:162px}
.card-bystander p{position:absolute;left:30px;width:221px;top:169px;text-align:center;color:var(--white);font-size:12px;line-height:19px}
.card-bystander .btn-read{position:absolute;left:76px;top:279px;width:128px;height:33px;border-radius:17px;background:var(--teal);color:var(--white);font-size:11.5px;font-weight:600;display:flex;align-items:center;justify-content:center}
.card-bully{left:780px;background:linear-gradient(160deg,#6f8a7a 0%,#4c6b66 50%,#2f4b58 100%)}
.card-bully h3{top:275px}

/* mission band */
.mission{position:absolute;left:0;top:1560px;width:1200px;height:400px;background:linear-gradient(100deg,#3b2f3a 0%,#2a2230 40%,#3a2a2c 70%,#5b2a38 100%)}
.mission p{position:absolute;left:300px;width:600px;top:136px;text-align:center;color:var(--white);font-size:23.5px;line-height:31px;font-weight:700}

/* resources */
.resources{position:absolute;left:0;top:1960px;width:1200px;height:418px}
.resources h2{position:absolute;left:0;width:1200px;top:75px;text-align:center;font-size:24px;font-weight:700}
.resource{position:absolute;top:139px;width:200px;height:200px}
.resource svg{display:block}
.resource span{position:absolute;left:0;width:200px;top:146px;text-align:center;font-size:13.5px;font-weight:700}
.r-lessons{left:152px}.r-workbooks{left:390px}.r-activities{left:620px;filter:drop-shadow(0 10px 18px rgba(0,0,0,.18))}.r-subject{left:859px}
.r-activities span{color:var(--white)}

/* footer */
.site-footer{position:absolute;left:0;top:2378px;width:1200px;height:337px;background:var(--footer);color:var(--footer-text)}
.footer-brand{position:absolute;left:141px;top:68px;font-size:22px;font-weight:700;color:var(--orange-a)}
.legal{position:absolute;left:141px;top:130px;font-size:11.5px;line-height:20px}
.footer-col h4{position:absolute;top:82px;font-size:14px;font-weight:600;color:var(--accent);white-space:nowrap}
.contact{left:391px}
.phone{position:absolute;left:391px;top:108px;font-size:18px}
.email{position:absolute;left:391px;top:138px;font-size:11.5px;line-height:20px;width:200px}
.address{position:absolute;left:391px;top:190px;font-size:11.5px;line-height:20px}
.quick-links{position:absolute;left:619px;top:108px;list-style:none;font-size:11.5px;line-height:24.5px}
.quick-links .current{color:var(--accent)}
.newsletter{position:absolute;left:860px;top:113px;width:199px;height:31px;background:#3b3738;border-radius:3px;font-size:11px;padding:9px 15px;color:#8d8d8d}
.newsletter svg{position:absolute;right:8px;top:7px}
.social{position:absolute;left:861px;top:161px;display:flex;gap:10px}
.social i{width:30px;height:30px;border-radius:50%;border:1.5px solid #8d8d8d;display:block}
</style>
</head>
<body>

<section class="hero">
  <div class="abs" role="img" aria-label="Photo of three young performers in white shirts and ties doing breakdance moves on a stage" style="inset:0"></div>
  <h1>Tumble Scholars<br>does Acrobatic<br>Educational Shows<br>for schools</h1>
  <div class="btn-hero">Book Now!</div>
</section>

<header class="site-header">
  <div class="brand">Tumble Scholars</div>
  <nav class="main-nav">
    <a class="current" style="left:0">Home</a>
    <a style="left:59px">About Us</a>
    <a style="left:139px">Our Program &amp; Shows</a>
    <a style="left:296px">Teachers Resources Portal</a>
  </nav>
  <a class="btn-book">Book your Shows!</a>
</header>

<section class="show-intro">
  <div class="halo"></div>
  <h2>Kindness-Shield<br>Tumbling Tour</h2>
  <p>Sed ut perspiciatis unde omnis iste natus error sit voluptatem accusantium doloremque laudantium, totam rem aperiam, eaque ipsa quae ab illo inventore veritatis et quasi architecto beatae vitae dicta sunt explicabo. Nemo enim ipsam voluptatem quia voluptas sit aspernatur aut odit aut fugit, sed quia consequuntur magni dolores.</p>
  <div class="explore">Explore More &nbsp;→</div>

  <article class="theme-card card-victim" role="img" aria-label="Photo of a young boy in glasses raising a finger">
    <h3>Educating the<br>Victim</h3>
    <div class="rule" style="top:325px"></div>
  </article>
  <article class="theme-card card-bystander" role="img" aria-label="Photo of a group of smiling children">
    <h3>Empowering the<br>Bystander</h3>
    <div class="rule"></div>
    <p>Lorem ipsum dolor sit amet, consectetur adipiscing elit, sed do eiusmod tempor incididunt ut labore et dolore ...</p>
    <div class="btn-read">Read More</div>
  </article>
  <article class="theme-card card-bully" role="img" aria-label="Photo of a pensive girl sitting outdoors">
    <h3>Enlightening<br>the Bully</h3>
  </article>
</section>

<section class="mission" role="img" aria-label="Photo of children dancing with an instructor on a stage">
  <p>Tumble Scholars engages children in important topics, by utilising Parkour &amp; Acro-batics to captivate and enthrall todays youngest generation.</p>
</section>

<section class="resources">
  <h2>Teachers Resources</h2>

  <div class="resource r-lessons">
    <svg width="200" height="200" viewBox="0 0 200 200">
      <defs><clipPath id="c1"><circle cx="100" cy="100" r="98"/></clipPath></defs>
      <circle cx="100" cy="100" r="98" fill="#fff" stroke="var(--yellow-soft)" stroke-width="2"/>
      <circle cx="100" cy="45" r="95" fill="var(--yellow)" clip-path="url(#c1)"/>
      <g fill="none" stroke="#fff" stroke-width="3" stroke-linejoin="round">
        <rect x="80" y="49" width="40" height="28"/><line x1="76" y1="49" x2="124" y2="49"/>
        <polyline points="87,70 96,61 103,66 113,56"/><line x1="100" y1="77" x2="92" y2="88"/><line x1="100" y1="77" x2="108" y2="88"/>
      </g>
    </svg>
    <span>Lesson Plans</span>
  </div>

  <div class="resource r-workbooks">
    <svg width="200" height="200" viewBox="0 0 200 200">
      <defs><clipPath id="c2"><circle cx="100" cy="100" r="98"/></clipPath></defs>
      <circle cx="100" cy="100" r="98" fill="#fff" stroke="var(--purple-soft)" stroke-width="2"/>
      <circle cx="100" cy="45" r="95" fill="var(--purple)" clip-path="url(#c2)"/>
      <g fill="none" stroke="#fff" stroke-width="3">
        <rect x="78" y="48" width="12" height="38"/><rect x="90" y="52" width="11" height="34"/><rect x="104" y="48" width="12" height="38"/>
        <line x1="74" y1="88" x2="124" y2="88"/>
      </g>
    </svg>
    <span>Workbooks</span>
  </div>

  <div class="resource r-activities">
    <svg width="200" height="200" viewBox="0 0 200 200">
      <defs><clipPath id="c3"><circle cx="100" cy="100" r="98"/></clipPath></defs>
      <circle cx="100" cy="100" r="98" fill="var(--green)" stroke="var(--green-soft)" stroke-width="2"/>
      <circle cx="100" cy="-4" r="95" fill="#fff" clip-path="url(#c3)"/>
      <g fill="none" stroke="var(--green)" stroke-width="3">
        <path d="M100 44c-14 0-24 10-24 22s10 22 22 22c5 0 5-5 3-8s0-7 5-7h6c7 0 12-4 12-11 0-10-10-18-24-18z"/>
        <circle cx="89" cy="58" r="3"/><circle cx="100" cy="53" r="3"/><circle cx="111" cy="58" r="3"/>
      </g>
    </svg>
    <span>Activities</span>
  </div>

  <div class="resource r-subject">
    <svg width="200" height="200" viewBox="0 0 200 200">
      <defs><clipPath id="c4"><circle cx="100" cy="100" r="98"/></clipPath></defs>
      <circle cx="100" cy="100" r="98" fill="#fff" stroke="var(--grey-soft)" stroke-width="2"/>
      <circle cx="100" cy="45" r="95" fill="var(--grey)" clip-path="url(#c4)"/>
      <g fill="none" stroke="#fff" stroke-width="3">
        <rect x="90" y="44" width="20" height="20"/><rect x="79" y="66" width="20" height="20"/><rect x="101" y="66" width="20" height="20"/>
      </g>
      <g fill="#fff" font-family="Montserrat,sans-serif" font-size="12" font-weight="700" text-anchor="middle">
        <text x="100" y="59">A</text><text x="89" y="81">B</text><text x="111" y="81">C</text>
      </g>
    </svg>
    <span>Subject</span>
  </div>
</section>

<footer class="site-footer">
  <div class="footer-brand">Tumble Scholars</div>
  <div class="legal">© 2018 Tumble Scholars. All rights<br>reserved.</div>

  <div class="footer-col"><h4 style="left:391px">Quick Contact</h4></div>
  <div class="phone">P. 1300 555 018</div>
  <div class="email">e. bookings@tumblescholars.<br>example</div>
  <div class="address">Tumble Scholars<br>Sydney NSW,<br>Australia</div>

  <div class="footer-col"><h4 style="left:619px">Quick Contact</h4></div>
  <ul class="quick-links">
    <li class="current">About Us</li>
    <li>Our Program and Shows</li>
    <li>Teachers Resources</li>
    <li>Contact</li>
  </ul>

  <div class="footer-col"><h4 style="left:860px">Stay Connected</h4></div>
  <div class="newsletter">Your Email ...
    <svg width="17" height="17" viewBox="0 0 17 17"><circle cx="8.5" cy="8.5" r="7.5" fill="none" stroke="#9b9b9b" stroke-width="1.3"/><polyline points="7,5 10.5,8.5 7,12" fill="none" stroke="#9b9b9b" stroke-width="1.3"/></svg>
  </div>
  <div class="social"><i></i><i></i><i></i><i></i></div>
</footer>

</body>
</html>
```